Redesign our existing zestHUB mobile app Dashboard & Login Screen

Revamp our existing dashboard design with new features added. New design should take into consideration that we already have existing users.
Design must be applicable to both Android and IOS.
The design should be vibrant, and attractive. Should not be too serious, old and bored. We are revamping the current design because, it was first released about 5 years ago, and when there are new additions, it was added by our developers. (you will notice the clock in and out button design is from our developers)
Our users will use this app every month to check their payslip as well as when they want to apply for vacation leave. Hence, there must be some personal touch to it - maybe display a photo?
Lastly, if possible, please also design a new Login Screen where employee's photo or company logo is displayed.
Reason: Hope to receive more designs before making final decision.
Target Market(s)
Working Adults (our existing users)
Font styles to use
Other font styles liked:
- Open Sans
Colors
Designer to choose colors to be used in the design.
Requirements
Must have
- Must have 7 options clearly displayed:-
- - My Profile, My Payroll, My Leave, My Claims, My Overtime, My TMS, My Utilities
- (you can remove the word MY - seems repetitive)
- Must have a notification to inform user who's on Leave/Vacation, upcoming Birthdays, new employees joining or those leaving the company.
- Bulletin to allow users to view company announcements/policies
- Must have button to clock in & out
Nice to have
- To-Do List where user will be able to see their pending tasks
- such as Leave Approval, Claims Approval, Overtime Approval

```html
<!DOCTYPE html>
<html lang="en">
<head>
<meta charset="utf-8">
<title>Employee Dashboard</title>
<link rel="stylesheet" href="https://fonts.googleapis.com/css2?family=Open+Sans:wght@300;400;600&display=swap">
<style>
  :root {
    --page: #e9e4df;
    --screen: #f6eee6;
    --tile: #fbf5ef;
    --accent: #f0386b;
    --ink: #2a2f45;
    --muted: #9a968f;
  }
  * { box-sizing: border-box; margin: 0; padding: 0; }
  html, body { width: 1200px; height: 1200px; overflow: hidden; }
  body {
    background: var(--page);
    font-family: "Open Sans", sans-serif;
    color: var(--ink);
    position: relative;
  }
  .screen {
    position: absolute; left: 290px; top: 50px;
    width: 620px; height: 1100px;
    background: var(--screen);
    display: flex; flex-direction: column;
    box-shadow: 0 10px 40px rgba(0,0,0,.12);
  }
  .status-bar {
    height: 36px; padding: 0 18px;
    display: flex; align-items: center; justify-content: space-between;
    font-size: 15px; font-weight: 400;
  }
  .status-bar .signal { display: flex; align-items: center; gap: 3px; }
  .dot { width: 7px; height: 7px; border-radius: 50%; background: var(--ink); }
  .dot.empty { background: none; border: 1px solid var(--ink); }
  .battery { display: flex; align-items: center; gap: 6px; }
  .battery-cell { width: 28px; height: 13px; border: 1px solid var(--ink); border-radius: 2px; padding: 1px; }
  .battery-cell span { display: block; width: 45%; height: 100%; background: var(--ink); }
  .greeting {
    height: 100px; margin: 0 10px; padding: 22px 22px 0;
    background: var(--tile);
    display: flex; justify-content: space-between; align-items: flex-start;
  }
  .greeting h1 { font-size: 30px; font-weight: 400; letter-spacing: -.3px; }
  .greeting p { font-size: 13px; color: var(--muted); margin-top: 4px; font-weight: 300; }
  .close-btn {
    width: 54px; height: 54px; border-radius: 50%;
    border: 1.5px solid var(--accent);
    display: flex; align-items: center; justify-content: center;
  }
  .dashboard {
    flex: 1; padding: 10px;
    display: grid; gap: 10px;
    grid-template-columns: 1fr 1fr;
    grid-template-rows: 300px 290px 1fr 1fr 120px;
  }
  .tile {
    background: var(--tile);
    display: flex; align-items: center; justify-content: center;
    font-size: 30px; font-weight: 300; color: var(--ink);
  }
  .tile.big { flex-direction: column; gap: 20px; }
  .ring {
    border: 1.5px solid var(--accent); border-radius: 50%;
    display: flex; align-items: center; justify-content: center;
  }
  .big .ring { width: 200px; height: 200px; }
  .dollar { font-size: 110px; font-weight: 600; color: var(--accent); line-height: 1; }
  .leave-row { grid-column: 1 / 3; display: grid; grid-template-columns: 45% 1fr; gap: 10px; }
  .leave-row .ring { width: 130px; height: 130px; }
  .leave-row .stack { display: grid; grid-template-rows: 1fr 1fr; gap: 10px; }
  .tile.inline { gap: 22px; }
  .wide { grid-column: 1 / 3; gap: 14px; }
  .clock-row { grid-column: 1 / 3; display: grid; grid-template-columns: repeat(3, 1fr); gap: 10px; }
  .clock-row .ring { width: 84px; height: 84px; }
  .clock-row .tile { gap: 16px; }
</style>
</head>
<body>
  <main class="screen">
    <div class="status-bar">
      <div class="signal">
        <span class="dot"></span><span class="dot"></span><span class="dot"></span><span class="dot empty"></span><span class="dot empty"></span>
        <span style="margin-left:4px">Carrier</span>
        <svg width="18" height="14" viewBox="0 0 18 14" style="margin-left:6px"><path d="M1 5a12 12 0 0 1 16 0M4 8a8 8 0 0 1 10 0M7 11a4 4 0 0 1 4 0" fill="none" stroke="#2a2f45" stroke-width="2"/></svg>
      </div>
      <span>9:41 AM</span>
      <div class="battery"><span>42%</span><div class="battery-cell"><span></span></div></div>
    </div>

    <header class="greeting">
      <div>
        <h1>Hello Marco Bellini,</h1>
        <p>Last login was on 27/07 at 2:34 pm.</p>
      </div>
      <div class="close-btn">
        <svg width="18" height="18" viewBox="0 0 18 18"><path d="M3 3l12 12M15 3L3 15" stroke="var(--accent)" stroke-width="2"/></svg>
      </div>
    </header>

    <section class="dashboard">
      <div class="tile big">
        <div class="ring">
          <svg width="90" height="100" viewBox="0 0 90 100"><circle cx="45" cy="30" r="20" fill="var(--accent)"/><path d="M10 95v-15a20 20 0 0 1 20-20h30a20 20 0 0 1 20 20v15z" fill="var(--accent)"/></svg>
        </div>
        <span>Profile</span>
      </div>
      <div class="tile big">
        <div class="ring"><span class="dollar">$</span></div>
        <span>Payroll</span>
      </div>

      <div class="leave-row">
        <div class="tile big">
          <div class="ring">
            <svg width="80" height="50" viewBox="0 0 80 50"><path d="M0 50L30 8l14 20 10-12 26 34z" fill="var(--accent)"/></svg>
          </div>
          <span>Leave</span>
        </div>
        <div class="stack">
          <div class="tile inline">
            <svg width="30" height="38" viewBox="0 0 30 38"><path d="M0 0h20l10 10v28H0z" fill="var(--accent)"/><path d="M6 18h18M6 24h18M6 30h12" stroke="#fbf5ef" stroke-width="2.5"/></svg>
            <span>Claims</span>
          </div>
          <div class="tile inline">
            <svg width="28" height="40" viewBox="0 0 28 40"><path d="M0 0h28v5h-3l-8 15 8 15h3v5H0v-5h3l8-15L3 5H0z" fill="var(--accent)"/></svg>
            <span>Overtime</span>
          </div>
        </div>
      </div>

      <div class="tile wide">
        <svg width="44" height="44" viewBox="0 0 44 44"><circle cx="22" cy="24" r="18" fill="var(--accent)"/><circle cx="22" cy="24" r="12" fill="none" stroke="#fbf5ef" stroke-width="2.5"/><path d="M22 24L16 17" stroke="#fbf5ef" stroke-width="3"/><rect x="18" y="0" width="8" height="5" fill="var(--accent)"/></svg>
        <span>TMS</span>
      </div>
      <div class="tile wide">
        <svg width="42" height="42" viewBox="0 0 42 42"><g fill="var(--accent)"><circle cx="21" cy="21" r="13"/><rect x="17" y="1" width="8" height="40"/><rect x="1" y="17" width="40" height="8"/><rect x="17" y="1" width="8" height="40" transform="rotate(45 21 21)"/><rect x="17" y="1" width="8" height="40" transform="rotate(-45 21 21)"/></g><circle cx="21" cy="21" r="6" fill="#fbf5ef"/></svg>
        <span>Utilities</span>
      </div>

      <div class="clock-row">
        <div class="tile">
          <div class="ring">
            <svg width="40" height="36" viewBox="0 0 40 36"><rect x="2" y="2" width="5" height="32" fill="var(--accent)"/><path d="M12 18L28 4v9h10v10H28v9z" fill="var(--accent)"/></svg>
          </div>
          <span>In</span>
        </div>
        <div class="tile">
          <div class="ring">
            <svg width="46" height="44" viewBox="0 0 46 44"><path d="M23 0l6.8 14.5L46 16.8 34 27.8 37 44 23 36 9 44l3-16.2L0 16.8l16.2-2.3z" fill="var(--accent)"/></svg>
          </div>
        </div>
        <div class="tile">
          <span>Out</span>
          <div class="ring">
            <svg width="40" height="36" viewBox="0 0 40 36"><rect x="33" y="2" width="5" height="32" fill="var(--accent)"/><path d="M28 18L12 4v9H2v10h10v9z" fill="var(--accent)"/></svg>
          </div>
        </div>
      </div>
    </section>
  </main>
</body>
</html>
```